Easy Business Card / Presentation Cover Design Project

We are looking for a business card design, covers for powerpoint presentations for investors, and possibly simple stationary for a Chicago real estate development firm. Our new logo is attached below.

We rehab and provide newly constructed homes. We are not a real estate brokerage firm (i.e., agents such as Meridale 47) and only operate in the Chicago area.

In terms of design, sophisticated and high end that would appeal to investors (theme should resemble investment banks, hedge funds, private equity rather than tech startup).

Target Market(s)

Investors, banks, financing sources

Industry/Entity Type

Real Estate

Requirements
Must have
• Two deliverables here. 1) Business card 2) Covers for powerpoint presentation.

Must be able to look sophisticated and high end when printed. Please think through the type of printing that will be needed. Would prefer something that can be printed in raised ink but digital is ok as well.

Will be printed on heavy paper.

Business Card: Horizontal Layout, no black backgrounds,

For presentation front cover, should include logo only. For back cover, should include contact info. Horizontal and should not contain any information that will need to be changed (i.e. date or client name)
Nice to have
• Would like to have the edges colored but not required. Please show multiple designs
Should not have
• Should not have any die cut or embossed type of designs. Shape should be standard size.

We are not a design firm, a retail firm, or a consumer product firm.

Please do not incorporate a house, buildings, etc. This must be very professional looking.

```html
<!DOCTYPE html>
<html lang="en">
<head>
<meta charset="utf-8">
<title>Ashvale Realty – Business Card</title>
<link href="https://fonts.googleapis.com/css2?family=Arvo:wght@400;700&display=swap" rel="stylesheet">
<style>
  :root {
    --backdrop: #2b2b2b;
    --card-light: #fbfbfb;
    --card-shade: #dcdcdc;
    --ink-gray: #5a5a5a;
    --ink-dark: #3c3c3c;
    --accent-blue: #3f8fd8;
    --skyline-top: rgba(200, 204, 210, 0);
    --skyline-mid: rgba(175, 180, 188, 0.4);
    --skyline-low: rgba(140, 146, 154, 0.5);
  }
  * { margin: 0; padding: 0; box-sizing: border-box; }
  html, body {
    width: 1200px; height: 900px; overflow: hidden;
    background: var(--backdrop);
    font-family: "Arvo", "Rockwell", serif;
  }
  .stage { position: relative; width: 1200px; height: 900px; }
  .card {
    position: absolute; top: 300px;
    width: 525px; height: 300px;
    border-radius: 30px;
    overflow: hidden;
    background: radial-gradient(ellipse at 40% 30%, var(--card-light) 0%, #f0f0f0 55%, var(--card-shade) 100%);
  }
  .card--front { left: 50px; }
  .card--back { left: 625px; }

  .brand { position: absolute; display: flex; align-items: center; gap: 14px; white-space: nowrap; }
  .brand__dot { width: 78px; height: 78px; border-radius: 50%; background: var(--accent-blue); flex: none; }
  .brand__name { color: var(--ink-gray); font-weight: 400; line-height: 0.95; text-transform: uppercase; }
  .card--front .brand { left: 52px; top: 62px; }
  .card--front .brand__name { font-size: 34px; }

  .skyline {
    position: absolute; left: 0; right: 0; bottom: 0; height: 175px;
    background: linear-gradient(to bottom, var(--skyline-top) 0%, var(--skyline-mid) 55%, var(--skyline-low) 100%);
  }
  .front-url {
    position: absolute; right: 30px; top: 218px;
    color: var(--accent-blue); font-size: 13px; font-weight: 700; letter-spacing: 0.5px;
  }

  .card--back .brand { left: 28px; top: 118px; gap: 10px; }
  .card--back .brand__dot { width: 58px; height: 58px; }
  .card--back .brand__name { font-size: 25px; }

  .divider {
    position: absolute; left: 252px; top: 72px;
    width: 2px; height: 160px; background: var(--accent-blue);
  }
  .contact {
    position: absolute; left: 268px; top: 74px; right: 18px;
    color: var(--ink-dark); font-size: 12.5px; line-height: 1.35; white-space: nowrap;
  }
  .contact__company { color: var(--accent-blue); font-weight: 700; font-size: 15px; line-height: 1.2; }
  .contact__sub { margin-bottom: 14px; }
  .contact__address { margin-bottom: 14px; }
  .contact__label { color: var(--accent-blue); }
  .contact__email { font-weight: 700; }
  .contact__web { color: var(--accent-blue); font-weight: 700; }
  .contact__row span + span { margin-left: 10px; }
</style>
</head>
<body>
<main class="stage">
  <section class="card card--front" aria-label="Business card front">
    <div class="skyline" role="img" aria-label="Faded photograph of the city skyline"></div>
    <div class="brand">
      <span class="brand__dot"></span>
      <span class="brand__name">Ashvale<br>Realty</span>
    </div>
    <p class="front-url">www.ashvalerealty.com</p>
  </section>

  <section class="card card--back" aria-label="Business card back">
    <div class="brand">
      <span class="brand__dot"></span>
      <span class="brand__name">Ashvale<br>Realty</span>
    </div>
    <div class="divider"></div>
    <div class="contact">
      <p class="contact__company">Ashvale Realty LLC</p>
      <p class="contact__sub">Northbrook Homebuilders LLC</p>
      <p class="contact__address">4280 N. Harlan Avenue, Suite 200<br>Chicago, IL 60641</p>
      <p class="contact__row"><span><span class="contact__label">T:</span> 312.555.0148</span><span><span class="contact__label">F:</span> 312.555.0192</span></p>
      <p><span class="contact__label">E:</span> <span class="contact__email">salesinfo</span>@ashvalerealty.com</p>
      <p class="contact__web">www.ashvalerealty.com</p>
    </div>
  </section>
</main>
</body>
</html>
```